FOLDER

I need a fine folder that will contain other items like brochures, flyers etc. This folder will be used to reach potential customers. The project will also include letter head
Updates

Please provide the following:
1. While we have the small envelop also include a big envelop that will contain the folder.
2. Please design a letterhead
3. Include in the design:
- Company name: TK Sparkwell & Facility Services Nigeria Limited.
- Our Logo. I have attached it.
- Moto: Setting new cleaning standards...
- Website: www.tk-sparkwell.com.ng
- E-mail: nigeria@tk-sparkwell.com
- Tel: 08097362418, 07061938274
Please give the size / dimensions of your designs (width and height).

Target Market(s)

households, offices etc. The business is cleaning and facility services

Requirements
Must have
• Please provide the following:
3. Include in the design:

```html
<!DOCTYPE html>
<html lang="en">
<head>
<meta charset="utf-8">
<title>TK Sparkwell – Folder Inside</title>
<link href="https://fonts.googleapis.com/css2?family=Cabin:wght@400;600&display=swap" rel="stylesheet">
<style>
  :root {
    --stage: #97a0a4;
    --paper: #ffffff;
    --brand-blue: #0b2fd8;
    --band-grey: #e9ecec;
    --ink: #3a3a3a;
    --spine: #6f7579;
    --dim-ink: #ffffff;
  }
  * { margin: 0; padding: 0; box-sizing: border-box; }
  html, body { width: 1200px; height: 900px; overflow: hidden; }
  body {
    background: var(--stage);
    font-family: "Cabin", "Gill Sans", sans-serif;
    color: var(--ink);
    position: relative;
  }
  .view-label {
    position: absolute; left: 124px; top: 54px;
    color: var(--dim-ink); font-size: 21px; letter-spacing: 1px;
  }
  .folder {
    position: absolute; left: 129px; top: 99px; width: 920px; height: 682px;
    filter: drop-shadow(4px 6px 4px rgba(0,0,0,.45));
  }
  .folder-art { position: absolute; inset: 0; }

  .panel-left { position: absolute; left: 0; top: 0; width: 452px; height: 682px; }
  .intro-title {
    position: absolute; left: 47px; top: 106px;
    color: var(--brand-blue); font-size: 16px; font-weight: 400;
  }
  .intro-band {
    position: absolute; left: 0; top: 139px; width: 452px; height: 229px;
    background: var(--band-grey);
    padding: 17px 48px 0 48px;
    font-size: 7.4px; line-height: 1.38;
  }
  .intro-lead { margin-bottom: 14px; }
  .intro-columns { display: flex; gap: 22px; }
  .intro-columns .col { width: 170px; }
  .intro-columns p { margin-bottom: 10px; }
  .intro-columns b { font-weight: 600; }
  .intro-columns i { display: block; }

  .wordmark { color: var(--brand-blue); font-weight: 600; display: flex; align-items: center; }
  .wordmark .dot { border-radius: 50%; background: currentColor; display: inline-block; }

  .front-brand {
    position: absolute; left: 47px; top: 548px; color: var(--paper);
  }
  .front-brand .wordmark { color: var(--paper); font-size: 24px; gap: 10px; }
  .front-brand .dot { width: 18px; height: 18px; }
  .motto { margin-top: 14px; font-size: 15px; color: var(--paper); }

  .panel-right { position: absolute; left: 466px; top: 0; width: 454px; height: 682px; }
  .pocket-id {
    position: absolute; left: 0; top: 212px; width: 454px; text-align: center;
  }
  .pocket-id .wordmark { justify-content: center; font-size: 24px; gap: 9px; }
  .pocket-id .dot { width: 16px; height: 16px; }
  .company-line { margin-top: 22px; font-size: 8.4px; }

  .business-card {
    position: absolute; left: 613px; top: 534px; width: 178px; height: 104px;
    background: var(--paper);
    box-shadow: 4px 5px 5px rgba(0,0,0,.55);
    text-align: center; padding-top: 24px;
  }
  .business-card .wordmark { justify-content: center; font-size: 15px; gap: 5px; }
  .business-card .dot { width: 10px; height: 10px; }
  .business-card .company-line { margin-top: 16px; font-size: 5.4px; }
  .card-slits { position: absolute; left: 600px; top: 520px; overflow: visible; }

  .dims { position: absolute; inset: 0; pointer-events: none; }
  .dim-label { position: absolute; color: var(--dim-ink); font-size: 21px; letter-spacing: 1px; }
  .dim-height { left: 52px; top: 446px; transform: rotate(-90deg); }
  .dim-width { left: 319px; top: 831px; }
  .dim-spine { left: 562px; top: 844px; }
  .dim-pocket { left: 1079px; top: 670px; transform: rotate(-90deg); }
</style>
</head>
<body>
  <div class="view-label">inside</div>

  <div class="folder">
    <svg class="folder-art" width="920" height="682" viewBox="0 0 920 682">
      <rect x="0" y="0" width="452" height="682" fill="var(--paper)"/>
      <rect x="466" y="0" width="454" height="682" fill="var(--paper)"/>
      <line x1="453.5" y1="0" x2="453.5" y2="682" stroke="var(--spine)" stroke-width="1"/>
      <line x1="465.5" y1="0" x2="465.5" y2="682" stroke="var(--spine)" stroke-width="1"/>
      <path d="M0 482 H352 A100 100 0 0 1 452 582 V682 H0 Z" fill="var(--brand-blue)"/>
      <path d="M466 582 A100 100 0 0 1 566 482 H920 V682 H466 Z" fill="var(--brand-blue)"/>
    </svg>

    <section class="panel-left">
      <h1 class="intro-title">TK Sparkwell Systems</h1>
      <div class="intro-band">
        <p class="intro-lead">TK has at its disposal almost two decades of extensive experience in the cleaning industry and has developed all types of cleaning solutions for large, medium and small businesses.</p>
        <div class="intro-columns">
          <div class="col">
            <p>Experience has taught us that commercial facilities find it more cost-effective and practical to outsource their cleaning providers.</p>
            <p><i>The advantages are:</i></p>
            <p><b>The quality of service is more reliable.</b> The service is implemented according to an agreed schedule and under a strict quality control regimen. Our cleaning staff undergo intensive training to adhere to our strict quality standards.</p>
            <p><b>Cost-effective.</b> Professional cleaning services are more cost-effective in the long run. Companies save on staffing costs and avoid personnel staffing issues.</p>
          </div>
          <div class="col">
            <p><b>Confidentiality.</b> TK impresses upon all its personnel the importance of confidentiality and strict adherence to security rules and regulations. Our staff have no criminal records and understand the significance of trustworthiness and confidentiality.</p>
            <p><b>Flexibility.</b> TK provides cleaning services anytime, anywhere according to the client’s needs and requirements.</p>
          </div>
        </div>
      </div>
      <div class="front-brand">
        <div class="wordmark">TK Sparkwell <span class="dot"></span></div>
        <p class="motto">Setting new cleaning standards...</p>
      </div>
    </section>

    <section class="panel-right">
      <div class="pocket-id">
        <div class="wordmark">TK Sparkwell <span class="dot"></span></div>
        <p class="company-line">TK Sparkwell &amp; Facility Services Nigeria Limited</p>
      </div>
    </section>

    <div class="business-card">
      <div class="wordmark">TK Sparkwell <span class="dot"></span></div>
      <p class="company-line">TK Sparkwell &amp; Facility Services Nigeria Limited</p>
    </div>
    <svg class="card-slits" width="210" height="140" viewBox="0 0 210 140">
      <line x1="3" y1="40" x2="40" y2="4" stroke="#111" stroke-width="1.5"/>
      <line x1="159" y1="132" x2="198" y2="94" stroke="#111" stroke-width="1.5"/>
    </svg>
  </div>

  <svg class="dims" width="1200" height="900" viewBox="0 0 1200 900">
    <line x1="106" y1="103" x2="106" y2="781" stroke="var(--dim-ink)" stroke-width="1.5"/>
    <line x1="129" y1="817" x2="581" y2="817" stroke="var(--dim-ink)" stroke-width="1.5"/>
    <line x1="583" y1="836" x2="594" y2="836" stroke="var(--dim-ink)" stroke-width="1.5"/>
    <line x1="1078" y1="581" x2="1078" y2="781" stroke="var(--dim-ink)" stroke-width="1.5"/>
  </svg>
  <span class="dim-label dim-height">320mm</span>
  <span class="dim-label dim-width">215mm</span>
  <span class="dim-label dim-spine">5mm</span>
  <span class="dim-label dim-pocket">95mm</span>
</body>
</html>
```